Logo & Visitenkarte für Chirurg
Zielgruppe
Ich bin Chirurg und Oberarzt in einer Klinik, weiterhin habe ich eine ambulante Sprechstunde. Ich suche vor allem in Bezug auf die Sprechstunde ein Design, um Patienten und andere Ärzte als Überweiser anzusprechen.
Die Schwerpunkte der Sprechstunde liegen in der Diagnostik und Therapie von chirurgischen Krankheitsbildern vor allem der Weichteile wie Bauch/Darm, Brüche, Tumore, Wunden und Enddarmleiden wie Hämorrhoiden. Keine wesentliche Rolle spielen die Behandlung von Knochenbrüchen oder orthopädischen Krankheiten wie Gelenkersatz, da dieses nicht meinem Metier zugeordnet wird.
Zielgruppe sind alle Patienten mit genannten Krankheiten ab 18 Jahren und deren Hausärzte.
Aufgabenstellung
Das Design sollte Vertrauen und Verlässlichkeit ausstrahlen.

```html
<!DOCTYPE html>
<html lang="de">
<head>
<meta charset="utf-8">
<title>Velmora – Visitenkarte</title>
<link rel="stylesheet" href="https://fonts.googleapis.com/css2?family=Questrial&display=swap">
<style>
  :root {
    --stage: #c1c0be;
    --paper: #ffffff;
    --brand-blue: #1e86b5;
    --ink-gray: #6d6e71;
    --shadow: rgba(40, 40, 40, 0.55);
  }
  html, body {
    margin: 0;
    padding: 0;
    overflow: hidden;
  }
  body {
    width: 1200px;
    height: 1176px;
    background: var(--stage);
    position: relative;
    font-family: "Questrial", "Century Gothic", sans-serif;
  }
  .card {
    position: absolute;
    box-shadow: 10px 10px 8px var(--shadow);
  }
  .card--front {
    left: 210px;
    top: 62px;
    width: 769px;
    height: 487px;
    background: var(--paper);
  }
  .card--back {
    left: 214px;
    top: 598px;
    width: 773px;
    height: 490px;
    background: var(--brand-blue);
  }
  .wordmark {
    position: absolute;
    display: flex;
    align-items: center;
    letter-spacing: 0.06em;
    text-transform: uppercase;
    line-height: 1;
  }
  .wordmark__dot {
    display: block;
    border-radius: 50%;
    flex: none;
  }
  .card--front .wordmark {
    left: 42px;
    top: 48px;
    font-size: 62px;
    color: var(--ink-gray);
    gap: 18px;
  }
  .card--front .wordmark__dot {
    width: 46px;
    height: 46px;
    background: var(--brand-blue);
  }
  .card--back .wordmark {
    left: 74px;
    top: 195px;
    font-size: 92px;
    color: var(--paper);
    gap: 26px;
  }
  .card--back .wordmark__dot {
    width: 70px;
    height: 70px;
    background: var(--paper);
  }
  .holder {
    position: absolute;
    left: 374px;
    top: 270px;
  }
  .holder__name {
    margin: 0;
    font-size: 46px;
    font-weight: 400;
    color: var(--brand-blue);
    letter-spacing: 0.02em;
    line-height: 1;
  }
  .holder__position {
    margin: 14px 0 0 20px;
    font-size: 14px;
    letter-spacing: 0.3em;
    color: var(--ink-gray);
  }
  .address {
    position: absolute;
    left: 22px;
    top: 342px;
    display: flex;
    gap: 14px;
    font-size: 20px;
    line-height: 27px;
    color: var(--ink-gray);
    font-style: normal;
    letter-spacing: 0.02em;
  }
  .address svg { margin-top: -2px; }
  .contacts {
    position: absolute;
    left: 374px;
    top: 353px;
    margin: 0;
    padding: 0;
    list-style: none;
    font-size: 21px;
    color: var(--ink-gray);
    letter-spacing: 0.02em;
  }
  .contacts li {
    display: flex;
    align-items: center;
    gap: 11px;
    height: 27px;
    margin-bottom: 15px;
  }
  .contacts svg { width: 26px; height: 26px; flex: none; }
  .front-band {
    position: absolute;
    left: 374px;
    right: 0;
    bottom: 0;
    height: 10px;
    background: var(--brand-blue);
  }
</style>
</head>
<body>

<section class="card card--front" aria-label="Vorderseite">
  <div class="wordmark"><span class="wordmark__dot"></span><span>Velmora</span></div>

  <div class="holder">
    <h1 class="holder__name">NAME</h1>
    <p class="holder__position">POSITION</p>
  </div>

  <address class="address">
    <svg width="22" height="32" viewBox="0 0 22 32" aria-hidden="true">
      <path d="M11 1C5.5 1 1.5 5 1.5 10.3 1.5 17 11 31 11 31s9.5-14 9.5-20.7C20.5 5 16.5 1 11 1z" fill="var(--brand-blue)"/>
      <circle cx="11" cy="10.5" r="4" fill="#fff"/>
    </svg>
    <span>Your City Adress<br>Street LocationXXXX,<br>Germany</span>
  </address>

  <ul class="contacts">
    <li>
      <svg viewBox="0 0 26 26" aria-hidden="true">
        <circle cx="13" cy="13" r="11.5" fill="none" stroke="var(--brand-blue)" stroke-width="1.6"/>
        <path d="M8.5 7.5l2.5-.5 1.5 3.3-1.6 1.2c.8 1.7 2 2.9 3.6 3.7l1.3-1.5 3.2 1.6-.5 2.5c-5.5.3-10.3-4.6-10-10.3z" fill="var(--brand-blue)"/>
      </svg>
      <span>+00 000 000 00 000</span>
    </li>
    <li>
      <svg viewBox="0 0 26 26" aria-hidden="true">
        <rect x="1" y="5" width="24" height="16" fill="var(--brand-blue)"/>
        <path d="M1.5 5.5L13 14.5 24.5 5.5M1.5 20.5l8.5-7.5M24.5 20.5l-8.5-7.5" fill="none" stroke="#fff" stroke-width="1.4"/>
      </svg>
      <span>info@velmora.de</span>
    </li>
    <li>
      <svg viewBox="0 0 26 26" aria-hidden="true" fill="none" stroke="var(--brand-blue)" stroke-width="1.6">
        <circle cx="13" cy="13" r="11.5"/>
        <ellipse cx="13" cy="13" rx="5" ry="11.5"/>
        <path d="M1.5 13h23M13 1.5v23M3.5 7h19M3.5 19h19"/>
      </svg>
      <span>www.velmora.de</span>
    </li>
  </ul>

  <div class="front-band"></div>
</section>

<section class="card card--back" aria-label="Rückseite">
  <div class="wordmark"><span class="wordmark__dot"></span><span>Velmora</span></div>
</section>

</body>
</html>
```